zOS app - Personal finance : Loan Calculator

Hi,
I need an app design for an zOS application that respects the last Plumora guidelines :
https://devs.plumora.com/os/interface-rules/graphics/app-icon/

I speak english and french.

Design should include logo, splashscreen and 4 main features as detailed further.

This application is a loan calculator that computes monthly payments, amortization tables, credit capacity.

App desc, screens and old logo here : https://apps.plumora.com/us/app/debt-path-housing-estimator/id584213097?mt=8

1. SPIRIT
The ideas to express in the design : simplicity, reliability, efficiency.
Use of graphics instead of words/number is always better.

2. ICON
No text, no letter in the logo.
Existing logo is not modern, too detailed.

3. SPLASHSCREEN

4. COLOR / Design style
ZOS 10 style
Modern colours
If you need one color as base use the blue

5. FEATURES/APP PAGES
Attached are the current screens to adapt with the new design :

Must Have:
- Loan Calculator (1screen uploaded in 2 parts)
- Loan Amortization : yearly table, monthly table and export (2 screens roughly the same +1)
- Saved Loans (1 screen), feature improvement could be to display what is left to pay for all loans, see saved loans idea 1 and 2 (I prefer the design of idea 1).
- Credit Capacity (1 screen uploaded in 2 parts), see also the inspiration file to propose a more visual interface (with chart/graphics)

Nice to have :
- refinance calculator (1 screen uploaded in 2 parts)
- Market rates table (1 screen)

Target Market(s)

1. Professionals in finance, real estate, car where a loan can be proposed to their customers -
2. Individuals that want to apply for a loan

Industry/Entity Type

Loan

Font styles to use
Serif
Sans Serif

Requirements
Must have
• Icon (see App Icon Guidelines in uploaded files)
• Splashscreen
• 4 Top features : Loan Calculator, Loan amortization with export, Credit capacity, Saved loans.
Nice to have
• Other screens : Refinance calculator, Market rates table
• New ideas of features / interactions
Should not have
• skeumorphism
• a total rupture from the current design : current users of the app should enjoy the new design and recognize the app without being lost (or not if you have arguments)

```html
<!DOCTYPE html>
<html lang="en">
<head>
<meta charset="utf-8">
<title>Loan Calculator</title>
<link rel="stylesheet" href="https://fonts.googleapis.com/css2?family=Roboto:wght@400;500&family=Cousine&display=swap">
<style>
  :root {
    --canvas-bg: #e6e7e8;
    --screen-bg: #f6f6f6;
    --card-bg: #ffffff;
    --ink: #1c1c1c;
    --ink-soft: #4a4a4a;
    --muted: #8a8a8a;
    --line: #dedede;
    --accent: #2196f3;
    --alert: #e2221f;
    --slice-principal: #f4cb12;
    --slice-interest: #5bdc12;
    --slice-insurance: #f46b70;
  }
  html, body {
    margin: 0;
    width: 1000px;
    height: 1200px;
    overflow: hidden;
    background: var(--canvas-bg);
  }
  .screen {
    position: absolute;
    left: 182px;
    top: 33px;
    width: 397px;
    height: 708px;
    transform: scale(1.6);
    transform-origin: 0 0;
    background: var(--screen-bg);
    font-family: "Roboto", sans-serif;
    color: var(--ink);
    overflow: hidden;
  }
  .abs { position: absolute; }
  .mono { font-family: "Cousine", monospace; }

  /* status bar */
  .status { left: 0; top: 0; width: 397px; height: 20px; font-size: 12px; font-weight: 500; }
  .status .signal { left: 7px; top: 7px; }
  .status .time { left: 0; width: 397px; top: 3px; text-align: center; }
  .status .battery-label { right: 32px; top: 3px; }
  .status .battery { right: 6px; top: 5px; }

  /* navigation */
  .nav-menu { left: 15px; top: 35px; }
  .nav-title { left: 0; width: 397px; top: 35px; text-align: center; font-size: 16px; letter-spacing: 0.2px; }

  /* card */
  .card {
    left: 11px; top: 67px; width: 376px; height: 629px;
    background: var(--card-bg); border-radius: 10px;
    box-shadow: 0 1px 4px rgba(0,0,0,0.18);
  }
  .rule { height: 1px; background: var(--line); }

  .amount { left: 0; width: 400px; top: 80px; text-align: center; font-size: 30px; }
  .currency { color: var(--muted); }
  .amount-currency { left: 357px; top: 86px; font-size: 21px; }

  .term-input {
    left: 26px; top: 131px; width: 104px; height: 51px;
    border: 1px solid #b9b9b9; border-radius: 6px;
    font-size: 20px; line-height: 51px; text-align: center; color: var(--ink-soft);
  }
  .term-unit { top: 150px; font-size: 16px; }
  .term-months { left: 229px; }
  .term-years { left: 317px; color: var(--accent); }
  .term-underline { left: 307px; top: 181px; width: 64px; height: 2px; background: var(--accent); }

  .rate { width: 188px; text-align: center; }
  .rate-value { top: 494px; }
  .rate .value { font-size: 30px; display: block; margin-top: 0; }
  .rate .label { font-size: 16px; color: var(--ink-soft); display: block; margin-top: 8px; }
  .rate .hint { font-size: 10.5px; color: var(--ink-soft); display: block; margin-top: 3px; }
  .rate-interest { left: 11px; top: 212px; }
  .rate-insurance { left: 199px; top: 212px; }
  .rate-divider { left: 199px; top: 223px; width: 1px; height: 57px; background: var(--line); }

  .row-label { left: 26px; font-size: 16px; }
  .row-value { right: 49px; font-size: 19px; text-align: right; }
  .row-currency { left: 367px; font-size: 16px; }

  .perforation { left: 11px; top: 364px; width: 376px; }

  .pie { left: 59px; top: 434px; }
  .legend-item { right: 79px; font-size: 16px; text-align: right; color: var(--ink-soft); }
  .legend-dot { left: 333px; width: 16px; height: 16px; border-radius: 50%; }

  .total-band {
    left: 11px; top: 590px; width: 376px; height: 53px;
    background: var(--accent); color: #fff;
  }
  .total-band .row-label { left: 15px; top: 17px; }
  .total-band .row-value { right: 20px; top: 15px; font-size: 20px; }
  .cost-value { color: var(--alert); }
</style>
</head>
<body>
<main class="screen">
  <div class="abs status">
    <svg class="abs signal" width="44" height="6" viewBox="0 0 44 6" aria-hidden="true">
      <circle cx="3" cy="3" r="2.8" fill="#111"/><circle cx="10" cy="3" r="2.8" fill="#111"/>
      <circle cx="17" cy="3" r="2.8" fill="#111"/><circle cx="24" cy="3" r="2.8" fill="#111"/>
      <circle cx="31" cy="3" r="2.8" fill="#111"/>
    </svg>
    <div class="abs time">9:41 AM</div>
    <div class="abs battery-label">100%</div>
    <svg class="abs battery" width="24" height="10" viewBox="0 0 24 10" aria-hidden="true">
      <rect x="0.5" y="0.5" width="21" height="9" rx="2" fill="none" stroke="#111"/>
      <rect x="2" y="2" width="18" height="6" rx="1" fill="#111"/>
      <rect x="22" y="3" width="1.6" height="4" fill="#111"/>
    </svg>
  </div>

  <svg class="abs nav-menu" width="28" height="18" viewBox="0 0 28 18" aria-label="Menu">
    <rect x="0" y="1" width="28" height="2" fill="#333"/>
    <rect x="0" y="8" width="22" height="2" fill="#333"/>
    <rect x="0" y="15" width="28" height="2" fill="#333"/>
  </svg>
  <div class="abs nav-title">LOAN CALCULATOR</div>

  <div class="abs card"></div>

  <div class="abs amount mono">200 000,00</div>
  <div class="abs amount-currency currency">€</div>

  <div class="abs term-input">20</div>
  <div class="abs term-unit term-months">months</div>
  <div class="abs term-unit term-years">years</div>
  <div class="abs term-underline"></div>

  <div class="abs rule" style="left:11px;top:195px;width:376px"></div>

  <div class="abs rate rate-interest">
    <span class="value mono">2,5</span>
    <span class="label">Interest (%)</span>
    <span class="hint">Nominal Annual Rate</span>
  </div>
  <div class="abs rate-divider"></div>
  <div class="abs rate rate-insurance">
    <span class="value mono">0,3</span>
    <span class="label">Insurance (%)</span>
    <span class="hint">Annual Rate (% of Loan Amount)</span>
  </div>

  <div class="abs rule" style="left:11px;top:306px;width:376px"></div>

  <div class="abs row-label" style="top:324px">One-Time Fee</div>
  <div class="abs row-value mono" style="top:321px">1 000,00</div>
  <div class="abs row-currency currency" style="top:324px">€</div>

  <svg class="abs perforation" width="376" height="2" viewBox="0 0 376 2" aria-hidden="true">
    <line x1="16" y1="1" x2="360" y2="1" stroke="#c8c8c8" stroke-width="1" stroke-dasharray="5 4"/>
  </svg>
  <svg class="abs" style="left:-2px;top:351px" width="26" height="28" viewBox="0 0 26 28" aria-hidden="true">
    <circle cx="13" cy="14" r="13" fill="#f6f6f6"/>
    <path d="M13 1 A13 13 0 0 1 13 27" fill="none" stroke="#d6d6d6"/>
  </svg>
  <svg class="abs" style="left:374px;top:351px" width="26" height="28" viewBox="0 0 26 28" aria-hidden="true">
    <circle cx="13" cy="14" r="13" fill="#f6f6f6"/>
    <path d="M13 1 A13 13 0 0 0 13 27" fill="none" stroke="#d6d6d6"/>
  </svg>

  <div class="abs row-label" style="top:387px">Monthly Payment</div>
  <div class="abs row-value mono" style="top:384px">1 109,81</div>
  <div class="abs row-currency currency" style="top:387px">€</div>

  <div class="abs rule" style="left:26px;top:421px;width:346px"></div>

  <svg class="abs pie" width="92" height="92" viewBox="-46 -46 92 92" role="img" aria-label="Payment split: principal 76%, interest 20%, insurance 4%">
    <circle cx="0" cy="0" r="46" fill="var(--slice-principal)"/>
    <path d="M0 0 L0 -46 A46 46 0 0 1 43.75 -14.21 Z" fill="var(--slice-interest)"/>
    <path d="M0 0 L-11.44 -44.56 A46 46 0 0 1 0 -46 Z" fill="var(--slice-insurance)"/>
  </svg>

  <div class="abs legend-item" style="top:439px">Insurance (4%)</div>
  <div class="abs legend-dot" style="top:441px;background:var(--slice-insurance)"></div>
  <div class="abs legend-item" style="top:471px">Interest (20%)</div>
  <div class="abs legend-dot" style="top:473px;background:var(--slice-interest)"></div>
  <div class="abs legend-item" style="top:503px">Principal (76%)</div>
  <div class="abs legend-dot" style="top:505px;background:var(--slice-principal)"></div>

  <div class="abs rule" style="left:26px;top:539px;width:346px"></div>

  <div class="abs row-label" style="top:556px">Total Cost of Credit</div>
  <div class="abs row-value mono cost-value" style="top:553px">67 353,39</div>
  <div class="abs row-currency currency" style="top:556px">€</div>

  <div class="abs total-band">
    <div class="abs row-label">Total Payments</div>
    <div class="abs row-value mono">267 353,39 €</div>
  </div>

  <div class="abs row-label" style="top:660px">Nominal APR</div>
  <div class="abs row-value mono" style="top:657px;right:26px">3,06 %</div>
</main>
</body>
</html>
```